Brochure Design Project

We need a brochure design.
It is an A3 page folded into 2 A4.
The brochure is for a company at the catering services in Israel - mostly finger food trays for businesses and home events.
Most of the brochure will be like a menu (we have the photos). To every photo there will be 3-4 short sentences that describes the food presented.
The brochure will be in Hebrew language (Right to Left) - We will do all the Language stuff but need an impressive design for the brochure.
The brochure should communicate quality and pleasent feelings.

Target Market(s)

1] Businesses Events - the person that orders food for Board meetings, courses, conventions - most of the time the secretaries.
2] Home Events - like birthdays, Celebrations - most of the time the mother orders the food

Industry/Entity Type

Catering

Requirements
Must have
• We have a logo and web site (so the main colors should communicate with it).
There are 5 categories: Main dishes, Salads, Deserts, Drinks, Extras

```html
<!DOCTYPE html>
<html lang="en">
<head>
<meta charset="utf-8">
<title>Royal Platter – Catering Menu Brochure</title>
<link href="https://fonts.googleapis.com/css2?family=Arimo:wght@400&display=swap" rel="stylesheet">
<style>
  :root {
    --sky-deep: #5f9fe0;
    --sky-mid: #a9cff3;
    --sky-light: #e6f2fc;
    --paper: #f7fbff;
    --ink: #2f3033;
    --heading: #2b2b2b;
    --rim: #3fae49;
    --accent-green: #8dc63f;
    --footer-wine: #4a1a24;
    --footer-text: #ffffff;
  }
  * { box-sizing: border-box; margin: 0; padding: 0; }
  html, body { width: 1200px; height: 841px; overflow: hidden; }
  body { font-family: "Arimo", Arial, sans-serif; color: var(--ink); }

  .brochure {
    position: relative;
    width: 1200px;
    height: 841px;
    overflow: hidden;
    background:
      radial-gradient(ellipse 520px 300px at 640px 90px, rgba(255,255,255,.85), rgba(255,255,255,0) 70%),
      radial-gradient(ellipse 700px 380px at 180px 760px, rgba(255,255,255,.95), rgba(255,255,255,0) 70%),
      linear-gradient(160deg, var(--sky-light) 0%, var(--sky-mid) 30%, var(--sky-deep) 55%, var(--sky-mid) 72%, var(--paper) 100%);
  }
  .brochure__swoosh { position: absolute; inset: 0; width: 1200px; height: 841px; }

  .section-title {
    position: absolute;
    font-size: 31px;
    font-weight: 400;
    text-decoration: underline;
    text-underline-offset: 4px;
    text-decoration-thickness: 2px;
    color: var(--heading);
    transform: translateX(-50%);
  }

  .blurb {
    position: absolute;
    text-align: right;
    white-space: nowrap;
  }
  .blurb--large { font-size: 15px; line-height: 19px; }
  .blurb--small { font-size: 8px; line-height: 10.4px; }

  .dish {
    position: absolute;
    border-radius: 50%;
    border: 1.5px solid var(--rim);
    box-shadow: 0 2px 4px rgba(0,0,0,.25);
  }
  .tone-tray    { background: radial-gradient(ellipse at 60% 60%, #e9c97a, #c9934a 45%, #5a3524 90%); }
  .tone-fruit   { background: radial-gradient(ellipse at 50% 50%, #f3d36a, #e6653f 40%, #8fb74a 75%, #f2efe2); }
  .tone-pastry  { background: radial-gradient(ellipse at 50% 40%, #f3c07a, #d98a3c 55%, #5b3325 92%); }
  .tone-cookies { background: radial-gradient(ellipse at 50% 40%, #e8d3a6, #9a6a45 55%, #3e2a22 92%); }
  .tone-salad   { background: radial-gradient(ellipse at 50% 50%, #d9c68c, #8aa84c 50%, #6b4a3a 90%); }
  .tone-cake    { background: radial-gradient(ellipse at 45% 45%, #f1e1c6, #c98b68 50%, #4d2e28 90%); }
  .tone-roll    { background: radial-gradient(ellipse at 50% 50%, #f0e4d2, #8a5a44 50%, #3a2620 90%); }
  .tone-greens  { background: radial-gradient(ellipse at 50% 50%, #b7d66a, #4f8a35 55%, #2f4f26 90%); }

  .footer-rule {
    position: absolute; left: 0; top: 810px; width: 1200px; height: 5px;
    background: var(--accent-green);
  }
  .footer-bar {
    position: absolute; left: 0; top: 815px; width: 1200px; height: 26px;
    background: var(--footer-wine);
    color: var(--footer-text);
    font-size: 12.5px;
    display: flex; justify-content: space-between; align-items: center;
    padding: 0 10px;
  }
</style>
</head>
<body>
<main class="brochure">
  <svg class="brochure__swoosh" viewBox="0 0 1200 841" aria-hidden="true">
    <path d="M380 300 C 600 200, 820 120, 1200 40" stroke="rgba(255,255,255,.55)" stroke-width="28" fill="none"/>
    <path d="M420 340 C 640 240, 860 180, 1200 120" stroke="rgba(255,255,255,.35)" stroke-width="12" fill="none"/>
    <path d="M500 420 C 700 330, 900 300, 1200 260" stroke="rgba(255,255,255,.3)" stroke-width="6" fill="none"/>
    <path d="M0 120 C 200 160, 380 240, 520 330" stroke="rgba(255,255,255,.25)" stroke-width="18" fill="none"/>
  </svg>

  <h2 class="section-title" style="left:497px; top:14px;">Salads</h2>
  <h2 class="section-title" style="left:1108px; top:18px;">Drinks</h2>
  <h2 class="section-title" style="left:512px; top:480px;">Deserts</h2>

  <!-- Featured column, left -->
  <p class="blurb blurb--large" style="left:0; width:396px; top:72px;">!Royal Platter Company Ltd is<br>one of the country's leading companies in the refreshment<br>and accommodation for offices and businesses.<br>Royal Platter, Ltd. operates in Israel for over twenty years</p>
  <p class="blurb blurb--large" style="left:0; width:396px; top:184px;">!Royal Platter Company Ltd is<br>one of the country's leading companies in the refreshment<br>and accommodation for offices and businesses.<br>Royal Platter, Ltd. operates in Israel for over twenty years</p>
  <p class="blurb blurb--large" style="left:0; width:396px; top:293px;">!Royal Platter Company Ltd is<br>one of the country's leading companies in the refreshment<br>and accommodation for offices and businesses.<br>Royal Platter, Ltd. operates in Israel for over twenty years</p>
  <p class="blurb blurb--large" style="left:0; width:396px; top:392px;">!Royal Platter Company Ltd is<br>one of the country's leading companies in the refreshment<br>and accommodation for offices and businesses.<br>Royal Platter, Ltd. operates in Israel for over twenty years</p>
  <div class="dish tone-tray" role="img" aria-label="Photo of a tray of assorted finger sandwiches" style="left:437px; top:66px; width:147px; height:96px;"></div>
  <div class="dish tone-fruit" role="img" aria-label="Photo of a fresh fruit platter" style="left:437px; top:173px; width:147px; height:96px;"></div>
  <div class="dish tone-pastry" role="img" aria-label="Photo of baked pastries on a tray" style="left:437px; top:278px; width:147px; height:96px;"></div>
  <div class="dish tone-cookies" role="img" aria-label="Photo of an assorted cookie tray" style="left:437px; top:382px; width:147px; height:96px;"></div>

  <!-- Drinks grid, top right -->
  <p class="blurb blurb--small" style="left:560px; width:253px; top:74px;">!Royal Platter Company Ltd is<br>one of the country's leading companies in the refreshment<br>and accommodation for offices and businesses.<br>Royal Platter, Ltd. operates in Israel for over twenty years</p>
  <p class="blurb blurb--small" style="left:560px; width:253px; top:144px;">!Royal Platter Company Ltd is<br>one of the country's leading companies in the refreshment<br>and accommodation for offices and businesses.<br>Royal Platter, Ltd. operates in Israel for over twenty years</p>
  <p class="blurb blurb--small" style="left:560px; width:253px; top:216px;">!Royal Platter Company Ltd is<br>one of the country's leading companies in the refreshment<br>and accommodation for offices and businesses.<br>Royal Platter, Ltd. operates in Israel for over twenty years</p>
  <p class="blurb blurb--small" style="left:560px; width:253px; top:288px;">!Royal Platter Company Ltd is<br>one of the country's leading companies in the refreshment<br>and accommodation for offices and businesses.<br>Royal Platter, Ltd. operates in Israel for over twenty years</p>
  <div class="dish tone-salad" role="img" aria-label="Photo of a mixed salad" style="left:816px; top:70px; width:77px; height:50px;"></div>
  <div class="dish tone-cake" role="img" aria-label="Photo of a sliced cake" style="left:816px; top:140px; width:77px; height:50px;"></div>
  <div class="dish tone-salad" role="img" aria-label="Photo of a mixed salad" style="left:816px; top:212px; width:77px; height:50px;"></div>
  <div class="dish tone-cake" role="img" aria-label="Photo of a sliced cake" style="left:816px; top:284px; width:77px; height:50px;"></div>

  <p class="blurb blurb--small" style="left:858px; width:253px; top:74px;">!Royal Platter Company Ltd is<br>one of the country's leading companies in the refreshment<br>and accommodation for offices and businesses.<br>Royal Platter, Ltd. operates in Israel for over twenty years</p>
  <p class="blurb blurb--small" style="left:858px; width:253px; top:144px;">!Royal Platter Company Ltd is<br>one of the country's leading companies in the refreshment<br>and accommodation for offices and businesses.<br>Royal Platter, Ltd. operates in Israel for over twenty years</p>
  <p class="blurb blurb--small" style="left:858px; width:253px; top:216px;">!Royal Platter Company Ltd is<br>one of the country's leading companies in the refreshment<br>and accommodation for offices and businesses.<br>Royal Platter, Ltd. operates in Israel for over twenty years</p>
  <p class="blurb blurb--small" style="left:858px; width:253px; top:288px;">!Royal Platter Company Ltd is<br>one of the country's leading companies in the refreshment<br>and accommodation for offices and businesses.<br>Royal Platter, Ltd. operates in Israel for over twenty years</p>
  <div class="dish tone-roll" role="img" aria-label="Photo of rolled pastries" style="left:1114px; top:70px; width:79px; height:50px;"></div>
  <div class="dish tone-greens" role="img" aria-label="Photo of a green leaf salad" style="left:1114px; top:140px; width:79px; height:50px;"></div>
  <div class="dish tone-roll" role="img" aria-label="Photo of rolled pastries" style="left:1114px; top:212px; width:79px; height:50px;"></div>
  <div class="dish tone-greens" role="img" aria-label="Photo of a green leaf salad" style="left:1114px; top:284px; width:79px; height:50px;"></div>

  <!-- Featured column, right -->
  <p class="blurb blurb--large" style="left:560px; width:433px; top:398px;">!Royal Platter Company Ltd is<br>one of the country's leading companies in the refreshment<br>and accommodation for offices and businesses.<br>Royal Platter, Ltd. operates in Israel for over twenty years</p>
  <p class="blurb blurb--large" style="left:560px; width:433px; top:511px;">!Royal Platter Company Ltd is<br>one of the country's leading companies in the refreshment<br>and accommodation for offices and businesses.<br>Royal Platter, Ltd. operates in Israel for over twenty years</p>
  <p class="blurb blurb--large" style="left:560px; width:433px; top:618px;">!Royal Platter Company Ltd is<br>one of the country's leading companies in the refreshment<br>and accommodation for offices and businesses.<br>Royal Platter, Ltd. operates in Israel for over twenty years</p>
  <p class="blurb blurb--large" style="left:560px; width:433px; top:716px;">!Royal Platter Company Ltd is<br>one of the country's leading companies in the refreshment<br>and accommodation for offices and businesses.<br>Royal Platter, Ltd. operates in Israel for over twenty years</p>
  <div class="dish tone-tray" role="img" aria-label="Photo of a tray of assorted finger sandwiches" style="left:1037px; top:387px; width:144px; height:94px;"></div>
  <div class="dish tone-fruit" role="img" aria-label="Photo of a fresh fruit platter" style="left:1037px; top:496px; width:144px; height:94px;"></div>
  <div class="dish tone-pastry" role="img" aria-label="Photo of baked pastries on a tray" style="left:1037px; top:603px; width:144px; height:94px;"></div>
  <div class="dish tone-cookies" role="img" aria-label="Photo of an assorted cookie tray" style="left:1037px; top:703px; width:144px; height:94px;"></div>

  <!-- Deserts grid, bottom left -->
  <p class="blurb blurb--small" style="left:0; width:218px; top:537px;">!Royal Platter Company Ltd is<br>one of the country's leading companies in the refreshment<br>and accommodation for offices and businesses.<br>Royal Platter, Ltd. operates in Israel for over twenty years</p>
  <p class="blurb blurb--small" style="left:0; width:218px; top:609px;">!Royal Platter Company Ltd is<br>one of the country's leading companies in the refreshment<br>and accommodation for offices and businesses.<br>Royal Platter, Ltd. operates in Israel for over twenty years</p>
  <p class="blurb blurb--small" style="left:0; width:218px; top:680px;">!Royal Platter Company Ltd is<br>one of the country's leading companies in the refreshment<br>and accommodation for offices and businesses.<br>Royal Platter, Ltd. operates in Israel for over twenty years</p>
  <p class="blurb blurb--small" style="left:0; width:218px; top:751px;">!Royal Platter Company Ltd is<br>one of the country's leading companies in the refreshment<br>and accommodation for offices and businesses.<br>Royal Platter, Ltd. operates in Israel for over twenty years</p>
  <div class="dish tone-salad" role="img" aria-label="Photo of a mixed salad" style="left:221px; top:533px; width:76px; height:50px;"></div>
  <div class="dish tone-cake" role="img" aria-label="Photo of a sliced cake" style="left:221px; top:605px; width:76px; height:50px;"></div>
  <div class="dish tone-salad" role="img" aria-label="Photo of a mixed salad" style="left:221px; top:676px; width:76px; height:50px;"></div>
  <div class="dish tone-cake" role="img" aria-label="Photo of a sliced cake" style="left:221px; top:747px; width:76px; height:50px;"></div>

  <p class="blurb blurb--small" style="left:300px; width:215px; top:537px;">!Royal Platter Company Ltd is<br>one of the country's leading companies in the refreshment<br>and accommodation for offices and businesses.<br>Royal Platter, Ltd. operates in Israel for over twenty years</p>
  <p class="blurb blurb--small" style="left:300px; width:215px; top:609px;">!Royal Platter Company Ltd is<br>one of the country's leading companies in the refreshment<br>and accommodation for offices and businesses.<br>Royal Platter, Ltd. operates in Israel for over twenty years</p>
  <p class="blurb blurb--small" style="left:300px; width:215px; top:680px;">!Royal Platter Company Ltd is<br>one of the country's leading companies in the refreshment<br>and accommodation for offices and businesses.<br>Royal Platter, Ltd. operates in Israel for over twenty years</p>
  <p class="blurb blurb--small" style="left:300px; width:215px; top:751px;">!Royal Platter Company Ltd is<br>one of the country's leading companies in the refreshment<br>and accommodation for offices and businesses.<br>Royal Platter, Ltd. operates in Israel for over twenty years</p>
  <div class="dish tone-roll" role="img" aria-label="Photo of rolled pastries" style="left:518px; top:533px; width:79px; height:50px;"></div>
  <div class="dish tone-greens" role="img" aria-label="Photo of a green leaf salad" style="left:518px; top:605px; width:79px; height:50px;"></div>
  <div class="dish tone-roll" role="img" aria-label="Photo of rolled pastries" style="left:518px; top:676px; width:79px; height:50px;"></div>
  <div class="dish tone-greens" role="img" aria-label="Photo of a green leaf salad" style="left:518px; top:747px; width:79px; height:50px;"></div>

  <div class="footer-rule"></div>
  <footer class="footer-bar">
    <span>Phone: 03-5550142</span>
    <span>Phone: 03-5550142</span>
  </footer>
</main>
</body>
</html>
```